依頼詳細
色々なホームページを参考に骨組みを作ってみました。
PDFファイルで添付しています。
2列から3列に変わると面白いのかなと思い、作りました。
もっと良い見せ方などがあれば自由に変更して頂いて構いません。

医院情報(院名・住所・診療時間)も添付資料をご覧ください。

ホームページには…
①まずは新患様に来ていただく(集客)
②医院の知名度の向上
このような効果を期待しています。

希望カラー…
建物の外装はこげ茶・白というモダンな作りです。
看板はオレンジ色です。
まだ医院が工事中で完成しておりませんが、
・完成イメージ
・現在出来上がっている院内
の写真を添付しておりますので、お色味の参考にして頂きたいです。

素材サイト:クモピクス「https://jp.kumopix.com/
このサイトの定期契約を当院で行いましたので
定期契約内で利用できる写真をデザイン内で使用してください。

他に必要なお写真がある場合には、無料で商用利用が出来るものを
ご利用頂ければと思います。

その他必要な情報などございましたらご質問ください。
楽しみにお待ちしております。宜しくお願い致します。
サイトURL
ページ数
1ページ
希望イメージ
シンプル 複雑
単色 カラフル
暗い 明るい
日常 高級
遊び心 厳粛
未来的 伝統的
女性的 男性的
希望する色
茶系、黄・オレンジ系、ベースカラーはクリーム色ぐらいのホワイトが希望です。
納品ファイル
• 高解像度JPG (.jpg)
• イラストレーター形式 (.ai)
• フォトショップ形式 (.psd)
• PNG形式 (.png)
補足説明
ランサーの皆さま

お世話になっております。
素敵なデザインをご提案頂き誠にありがとうございます。
とても嬉しいです!

期間が短く、申し訳ございません。
募集期間が延長出来るという事で、今日から1週間ほど期間を延長致します。

こちらの提出した骨組みから全く違う構成でももちろん構いませんので、
色んなパターンのデザインが見てみたいと思っています。
引き続きよろしくお願い致します。
■ 選んだ理由

一番当院のイメージに近く、一番要望に沿っているデザインだと感じたため。

■ 提案者全員のお礼・コメント

たくさんのデザインをご提案頂き、非常にうれしく思っております。
OPENに向けまずはトップデザインが決まり、わくわくしております。

この度は誠にありがとうございました。
これからも皆様のご活躍を、陰ながらではございますが、応援致しております。

```html
<!DOCTYPE html>
<html lang="ja">
<head>
<meta charset="utf-8">
<title>みどり歯科クリニック</title>
<link rel="stylesheet" href="https://fonts.googleapis.com/css2?family=Noto+Sans+JP:wght@400;500;700&family=Noto+Serif+JP:wght@500;700&display=swap">
<style>
:root{
  --orange:#ef8a1c;
  --orange-soft:#f6b35c;
  --orange-pale:#fdebd3;
  --brown:#6b4a2e;
  --brown-dark:#4a3220;
  --cream:#fbf6ec;
  --beige:#f3e7d3;
  --line:#e3d4bc;
  --text:#4b3a2b;
  --muted:#8a7865;
  --white:#ffffff;
  --map-a:#e6e2d8;
  --map-b:#cfc7b6;
}
*{box-sizing:border-box;margin:0;padding:0}
html,body{width:1200px;height:5068px;overflow:hidden}
body{background:var(--cream);font-family:"Noto Sans JP",sans-serif;color:var(--text);font-size:13px;line-height:1.6}
.wrap{width:1080px;margin:0 auto;position:relative}
/* header */
.site-header{height:244px;background:var(--white)}
.site-header .wrap{height:244px}
.tagline{position:absolute;top:14px;left:0;font-size:11px;color:var(--muted)}
.brand{position:absolute;top:42px;left:0;display:flex;align-items:center;gap:12px}
.brand-mark{width:44px;height:44px;border-radius:50%;background:var(--orange);flex:none}
.brand-name{font-size:34px;font-weight:700;color:var(--brown);white-space:nowrap}
.access-note{position:absolute;top:104px;left:0;font-size:11px;color:var(--muted);line-height:1.8}
.access-note b{background:var(--orange);color:#fff;padding:1px 6px;margin-right:6px;font-weight:500}
.hours-box{position:absolute;top:36px;right:0;width:340px;border:1px solid var(--line);font-size:11px}
.hours-box .hd{background:var(--brown);color:#fff;padding:3px 10px;display:flex;justify-content:space-between}
.hours-box .bd{padding:6px 10px;display:flex;justify-content:space-between;color:var(--text)}
.phone-box{position:absolute;top:112px;right:0;display:flex;align-items:center;gap:12px;white-space:nowrap}
.phone-box .lbl{background:var(--orange);color:#fff;font-size:10px;padding:4px 8px;line-height:1.4}
.phone-box .num{font-size:30px;font-weight:700;color:var(--brown);display:flex;align-items:center;gap:6px;line-height:1}
.global-nav{position:absolute;bottom:0;left:0;right:0;height:64px;display:flex;border-top:1px solid var(--line)}
.global-nav a{flex:1;text-align:center;text-decoration:none;color:var(--brown);font-weight:700;font-size:15px;padding-top:10px;border-right:1px solid var(--line)}
.global-nav a:last-child{border-right:0}
.global-nav a span{display:block;font-size:9px;color:var(--orange);font-weight:400;letter-spacing:.08em}
/* hero */
.hero{height:470px;position:relative;background:linear-gradient(90deg,#fbf6ec 0%,#f7efe2 30%,#e9dccb 100%)}
.hero-photo{position:absolute;left:300px;right:0;top:0;bottom:0;background:linear-gradient(135deg,#f3ece2 0%,#dcccb7 55%,#c9b49c 100%)}
.hero-copy{position:absolute;left:150px;top:40px;writing-mode:vertical-rl;font-family:"Noto Serif JP",serif;font-size:30px;font-weight:700;color:var(--brown-dark);line-height:1.7;letter-spacing:.12em;height:380px}
/* treatment bar */
.treat-bar{height:52px;background:var(--beige)}
.treat-bar .wrap{display:flex;align-items:center;height:52px;gap:10px}
.treat-bar .ttl{background:var(--white);color:var(--brown);font-weight:700;padding:6px 22px;margin-right:auto;font-size:13px}
.treat-bar a{background:var(--white);color:var(--brown);text-decoration:none;font-size:12px;padding:6px 16px;border:1px solid var(--line)}
.treat-bar a::before{content:"›";color:var(--orange);margin-right:6px}
/* columns */
.columns{display:flex;gap:40px;padding-top:60px;width:1080px;margin:0 auto;height:2660px}
.side{width:240px;flex:none}
.main{flex:1}
.side-btn{display:flex;align-items:center;gap:10px;background:var(--orange);color:#fff;font-weight:700;font-size:20px;padding:14px 18px;border-radius:4px;margin-bottom:20px}
.side-btn .ic{width:30px;height:30px;border-radius:50%;background:#fff}
.recruit-box{border:2px solid var(--orange);background:var(--white);padding:14px;margin-bottom:22px}
.recruit-box p{font-size:18px;font-weight:700;color:var(--brown);margin-bottom:10px;line-height:1.4}
.recruit-box .tag{background:var(--orange);color:#fff;text-align:center;font-size:13px;font-weight:700;padding:4px}
.side-head{background:var(--brown);color:#fff;font-size:12px;padding:6px 12px;margin-bottom:8px}
.value-item{display:flex;gap:10px;align-items:center;background:var(--white);border:1px solid var(--line);padding:10px;margin-bottom:8px}
.value-item .badge{width:46px;height:46px;flex:none;border-radius:6px;background:var(--orange);color:#fff;font-weight:700;display:flex;align-items:center;justify-content:center;font-size:14px}
.value-item p{font-size:11px;color:var(--muted);line-height:1.5}
.effort-box{background:var(--orange-pale);border:1px solid var(--orange-soft);padding:14px;margin:18px 0}
.effort-box h4{color:var(--orange);font-size:13px;margin-bottom:8px}
.effort-box li{list-style:none;font-size:11px;color:var(--text);padding:4px 0 4px 12px;border-bottom:1px dotted var(--orange-soft);position:relative}
.effort-box li::before{content:"›";position:absolute;left:0;color:var(--orange)}
.side-links{background:var(--white);border:1px solid var(--line);margin-bottom:20px}
.side-links a{display:block;padding:9px 14px;color:var(--text);text-decoration:none;font-size:12px;border-bottom:1px solid var(--line)}
.side-links a:last-child{border-bottom:0}
.side-links a::before{content:"›";color:var(--orange);margin-right:8px}
.treat-list{background:var(--white);border:1px solid var(--line);margin-bottom:40px}
.treat-list div{display:flex;align-items:center;gap:12px;padding:8px 10px;border-bottom:1px solid var(--line);font-size:12px;color:var(--brown)}
.treat-list div:last-child{border-bottom:0}
.treat-list .th{width:48px;height:40px;background:linear-gradient(135deg,#f1e6d6,#d9c6ad)}
.side-banner{display:flex;align-items:center;gap:12px;background:var(--white);border:1px solid var(--line);margin-bottom:14px;height:94px;padding:10px}
.side-banner .im{width:80px;height:72px;background:linear-gradient(135deg,#efe4d4,#cdb89e)}
.side-banner b{display:block;font-size:16px;color:var(--brown)}
.side-banner span{font-size:9px;color:var(--orange);letter-spacing:.1em}
/* main */
.feature-title{text-align:center;font-size:26px;font-weight:700;color:var(--brown);margin-bottom:26px}
.feature-title em{font-style:normal;color:var(--orange);font-size:40px;margin:0 4px}
.features{display:flex;gap:24px;margin-bottom:40px}
.feature{flex:1}
.feature .ph{height:150px;background:linear-gradient(135deg,#f2e8da,#d4bfa4);margin-bottom:12px}
.feature h3{font-size:16px;color:var(--brown);line-height:1.4;margin-bottom:6px}
.feature p{font-size:11px;color:var(--muted)}
.sec-head{font-size:20px;font-weight:700;color:var(--brown);border-bottom:2px solid var(--orange);padding-bottom:6px;margin-bottom:20px}
.greeting{display:flex;gap:26px;background:var(--white);border:1px solid var(--line);padding:24px;margin-bottom:36px}
.greeting .ph{width:260px;height:280px;flex:none;background:linear-gradient(160deg,#f3ece3,#c9b49b)}
.greeting h3{font-family:"Noto Serif JP",serif;font-size:20px;color:var(--brown-dark);line-height:1.5;margin-bottom:14px}
.greeting p{font-size:12px;color:var(--text);line-height:1.9;margin-bottom:12px}
.greeting .sign{text-align:right;font-size:13px;font-weight:700}
.more{display:inline-block;font-size:11px;color:var(--orange);margin-top:6px}
.trouble{display:grid;grid-template-columns:repeat(3,1fr);gap:12px;background:var(--beige);padding:20px;margin-bottom:36px}
.trouble div{display:flex;align-items:center;gap:12px;background:var(--white);border-radius:40px;padding:12px 16px;font-size:14px;font-weight:500;color:var(--brown);height:66px;line-height:1.4}
.trouble .ck{width:34px;height:34px;border-radius:50%;background:var(--orange);flex:none;display:flex;align-items:center;justify-content:center}
.menu-grid{display:grid;grid-template-columns:repeat(5,1fr);gap:14px;margin-bottom:24px}
.menu-grid figure{text-align:center;font-size:12px;color:var(--brown)}
.menu-grid .ph{height:130px;background:linear-gradient(135deg,#f2e7d8,#d2bca1);margin-bottom:6px}
.recruit-banner{display:flex;align-items:center;gap:20px;width:470px;margin-left:auto;background:var(--white);border:2px solid var(--orange);padding:10px;margin-bottom:40px}
.recruit-banner .ph{width:80px;height:60px;background:linear-gradient(135deg,#efe4d4,#cdb89e);flex:none}
.recruit-banner b{display:block;font-size:20px;color:var(--brown);white-space:nowrap}
.recruit-banner span{background:var(--orange);color:#fff;font-size:12px;padding:2px 12px}
.access{display:flex;gap:24px;margin-bottom:36px}
.access .left{width:390px;flex:none}
.hours{width:100%;border-collapse:collapse;font-size:11px;background:var(--white);margin-bottom:12px}
.hours th,.hours td{border:1px solid var(--line);padding:6px 4px;text-align:center;white-space:nowrap}
.hours th{background:var(--brown);color:#fff;font-weight:500}
.hours td.o{color:var(--orange)}
.tel{display:flex;align-items:center;gap:8px;font-size:28px;font-weight:700;color:var(--brown);white-space:nowrap}
.addr{font-size:11px;color:var(--muted);margin-bottom:12px}
.card-note{background:var(--white);border:1px solid var(--line);font-size:12px}
.card-note .hd{background:var(--beige);padding:6px 10px;font-weight:700;color:var(--brown)}
.card-note .bd{padding:10px;text-align:center;color:var(--text)}
.map-box{flex:1;height:300px;background:linear-gradient(135deg,var(--map-a),var(--map-b));display:flex;align-items:center;justify-content:center}
.news-cols{display:flex;gap:30px}
.news-cols section{flex:1}
.news-cols li{list-style:none;font-size:12px;padding:9px 0;border-bottom:1px dotted var(--line);display:flex;gap:14px}
.news-cols li time{color:var(--muted)}
.news-cols .all{display:inline-block;margin-top:12px;background:var(--white);border:1px solid var(--line);padding:5px 14px;font-size:11px;color:var(--brown)}
/* map band */
.map-band{height:680px;background:linear-gradient(135deg,var(--map-a) 0%,var(--map-b) 55%,#ddd6c8 100%);display:flex;align-items:center;justify-content:center}
/* footer */
.site-footer{background:var(--cream);height:962px;border-top:4px solid var(--orange);position:relative}
.site-footer .wrap{padding-top:60px}
.foot-brand{display:flex;align-items:center;gap:12px;margin-bottom:16px}
.foot-brand .brand-name{font-size:30px}
.foot-row{display:flex;justify-content:space-between;align-items:flex-start;margin-bottom:50px}
.foot-row .tel{font-size:30px;margin-bottom:6px}
.foot-row .hours{width:420px;font-size:12px}
.foot-links{display:grid;grid-template-columns:repeat(6,1fr);gap:22px 20px;border-top:1px solid var(--line);padding-top:40px}
.foot-links a{font-size:13px;color:var(--text);text-decoration:none}
.foot-links a::before{content:"›";color:var(--orange);margin-right:6px}
.copyright{position:absolute;bottom:0;left:0;right:0;height:60px;background:var(--brown);color:#fff;font-size:11px;display:flex;align-items:center;justify-content:center}
</style>
</head>
<body>
<header class="site-header">
  <div class="wrap">
    <p class="tagline">緑ヶ丘市の歯医者ならみどり歯科クリニック｜一般・小児・口腔外科・予防歯科</p>
    <div class="brand"><span class="brand-mark"></span><span class="brand-name">みどり歯科クリニック</span></div>
    <p class="access-note"><b>アクセス</b>さくら駅より徒歩5分・駐車場あり<br>〒000-0000 緑ヶ丘市さくら町1丁目2-3</p>
    <div class="hours-box">
      <div class="hd"><span>診療時間</span><span>休診日 木・日・祝</span></div>
      <div class="bd"><span>平日・土曜 9:00〜12:30</span><span>午後 14:30〜18:30</span></div>
    </div>
    <div class="phone-box">
      <span class="lbl">ホームページを見た<br>とお伝えください</span>
      <span class="num"><svg width="24" height="24" viewBox="0 0 24 24"><path fill="#ef8a1c" d="M6.6 10.8a15 15 0 0 0 6.6 6.6l2.2-2.2c.3-.3.7-.4 1-.2 1.1.4 2.3.6 3.6.6.6 0 1 .4 1 1V20c0 .6-.4 1-1 1A17 17 0 0 1 3 4c0-.6.4-1 1-1h3.5c.6 0 1 .4 1 1 0 1.3.2 2.5.6 3.6.1.3 0 .7-.2 1z"/></svg>0595-00-1234</span>
    </div>
    <nav class="global-nav">
      <a href="#">トップ<span>TOP</span></a>
      <a href="#">院長紹介<span>DIRECTOR</span></a>
      <a href="#">診療内容<span>MEDICAL CARE</span></a>
      <a href="#">設備紹介<span>EQUIPMENT</span></a>
      <a href="#">アクセス<span>ACCESS</span></a>
      <a href="#">患者様の声<span>VOICE</span></a>
      <a href="#">費用について<span>PRICE</span></a>
    </nav>
  </div>
</header>

<section class="hero">
  <div class="hero-photo" role="img" aria-label="歯の模型を手にした歯科医の写真"></div>
  <p class="hero-copy">自分の家族にも出来る、<br>安心安全な歯科医療を<br>目指します。</p>
</section>

<nav class="treat-bar">
  <div class="wrap">
    <span class="ttl">診療項目</span>
    <a href="#">一般歯科</a><a href="#">小児歯科</a><a href="#">義歯・入れ歯</a><a href="#">口腔外科</a><a href="#">インプラント治療</a><a href="#">予防歯科</a>
  </div>
</nav>

<div class="columns">
  <aside class="side">
    <div class="side-btn"><span class="ic"></span>初めての方へ</div>
    <div class="recruit-box">
      <p>私たちと一緒に<br>働きませんか？</p>
      <div class="tag">歯科医師・衛生士募集</div>
    </div>
    <div class="side-head">安心できる歯医者を目指して</div>
    <div class="value-item"><span class="badge">安心</span><p>カウンセリングをしっかり行います</p></div>
    <div class="value-item"><span class="badge">安全</span><p>充実した最新機器で的確な診療</p></div>
    <div class="value-item"><span class="badge">信頼</span><p>患者様のお話を丁寧にお伺いします</p></div>
    <div class="value-item"><span class="badge">清潔</span><p>院内の衛生管理を徹底しています</p></div>
    <div class="effort-box">
      <h4>当院の取り組み</h4>
      <ul>
        <li>インプラントで快適な噛み心地</li>
        <li>予防の重要性をお伝えします</li>
        <li>痛みの少ない治療を心がけます</li>
        <li>お子様も通いやすい環境づくり</li>
      </ul>
    </div>
    <nav class="side-links">
      <a href="#">初めての方へ</a><a href="#">設備紹介</a><a href="#">費用について</a>
    </nav>
    <div class="side-head">診療項目</div>
    <div class="treat-list">
      <div><span class="th" role="img" aria-label="一般歯科の写真"></span>一般歯科</div>
      <div><span class="th" role="img" aria-label="小児歯科の写真"></span>小児歯科</div>
      <div><span class="th" role="img" aria-label="入れ歯の写真"></span>入れ歯（義歯）</div>
      <div><span class="th" role="img" aria-label="口腔外科の写真"></span>口腔外科</div>
      <div><span class="th" role="img" aria-label="審美歯科の写真"></span>審美歯科</div>
      <div><span class="th" role="img" aria-label="矯正歯科の写真"></span>矯正歯科</div>
      <div><span class="th" role="img" aria-label="インプラントの写真"></span>インプラント治療</div>
      <div><span class="th" role="img" aria-label="予防歯科の写真"></span>予防歯科</div>
    </div>
    <div class="side-banner"><span class="im" role="img" aria-label="医院トピックスの写真"></span><div><b>医院トピックス</b><span>CLINIC TOPICS</span></div></div>
    <div class="side-banner"><span class="im" role="img" aria-label="新着情報の写真"></span><div><b>新着情報</b><span>NEWS</span></div></div>
    <div class="side-banner"><span class="im" role="img" aria-label="患者様の声の写真"></span><div><b>患者様の声</b><span>VOICE</span></div></div>
  </aside>

  <main class="main">
    <h2 class="feature-title">みどり歯科クリニックの<em>3</em>つの特徴</h2>
    <div class="features">
      <article class="feature"><div class="ph" role="img" aria-label="最新機器での治療の写真"></div><h3>最先端の低被ばく<br>歯科用CTを導入</h3><p>精密な診断で安全な治療を行います。</p></article>
      <article class="feature"><div class="ph" role="img" aria-label="笑顔の口元の写真"></div><h3>プチ矯正<br>見えない矯正</h3><p>目立たない装置で気軽に始められます。</p></article>
      <article class="feature"><div class="ph" role="img" aria-label="子どもの診察の写真"></div><h3>小児矯正<br>歯を抜かない歯列形成</h3><p>成長に合わせた無理のない治療です。</p></article>
    </div>

    <h2 class="sec-head">院長挨拶</h2>
    <div class="greeting">
      <div class="ph" role="img" aria-label="院長の写真"></div>
      <div>
        <h3>ご家族揃って安心して通える<br>歯科医院を目指して…</h3>
        <p>この度は、私の生まれ育ったこの町で歯科医院を開業することになりました。地域の皆様が気軽に相談でき、痛みの少ない丁寧な治療を受けられる医院づくりを心がけております。</p>
        <p>患者様一人ひとりのお話をしっかりお伺いし、納得いただける説明を大切にいたします。予防から治療まで、ご家族皆様の歯の健康を長くお守りできるよう努めてまいります。お気軽にご来院ください。</p>
        <p class="sign">院長　緑川 孝一郎</p>
        <span class="more">› 院長紹介へ</span>
      </div>
    </div>

    <h2 class="sec-head">このようなことでお困りではありませんか？</h2>
    <div class="trouble">
      <div><span class="ck"><svg width="16" height="16" viewBox="0 0 16 16"><path d="M3 8l3 3 7-7" stroke="#fff" stroke-width="2.4" fill="none"/></svg></span>冷たいものがしみる</div>
      <div><span class="ck"><svg width="16" height="16" viewBox="0 0 16 16"><path d="M3 8l3 3 7-7" stroke="#fff" stroke-width="2.4" fill="none"/></svg></span>歯茎から血が出る</div>
      <div><span class="ck"><svg width="16" height="16" viewBox="0 0 16 16"><path d="M3 8l3 3 7-7" stroke="#fff" stroke-width="2.4" fill="none"/></svg></span>子供の歯を守りたい</div>
      <div><span class="ck"><svg width="16" height="16" viewBox="0 0 16 16"><path d="M3 8l3 3 7-7" stroke="#fff" stroke-width="2.4" fill="none"/></svg></span>子供の歯並びが気になる</div>
      <div><span class="ck"><svg width="16" height="16" viewBox="0 0 16 16"><path d="M3 8l3 3 7-7" stroke="#fff" stroke-width="2.4" fill="none"/></svg></span>歯茎が腫れてうまく噛めない</div>
      <div><span class="ck"><svg width="16" height="16" viewBox="0 0 16 16"><path d="M3 8l3 3 7-7" stroke="#fff" stroke-width="2.4" fill="none"/></svg></span>白い歯を取り戻したい</div>
      <div><span class="ck"><svg width="16" height="16" viewBox="0 0 16 16"><path d="M3 8l3 3 7-7" stroke="#fff" stroke-width="2.4" fill="none"/></svg></span>親知らずが痛くて悩んでいる</div>
      <div><span class="ck"><svg width="16" height="16" viewBox="0 0 16 16"><path d="M3 8l3 3 7-7" stroke="#fff" stroke-width="2.4" fill="none"/></svg></span>口内炎がつらい</div>
      <div><span class="ck"><svg width="16" height="16" viewBox="0 0 16 16"><path d="M3 8l3 3 7-7" stroke="#fff" stroke-width="2.4" fill="none"/></svg></span>抜けた歯を元通りにしたい</div>
      <div><span class="ck"><svg width="16" height="16" viewBox="0 0 16 16"><path d="M3 8l3 3 7-7" stroke="#fff" stroke-width="2.4" fill="none"/></svg></span>入れ歯が合わず痛い</div>
      <div><span class="ck"><svg width="16" height="16" viewBox="0 0 16 16"><path d="M3 8l3 3 7-7" stroke="#fff" stroke-width="2.4" fill="none"/></svg></span>虫歯を予防したい</div>
      <div><span class="ck"><svg width="16" height="16" viewBox="0 0 16 16"><path d="M3 8l3 3 7-7" stroke="#fff" stroke-width="2.4" fill="none"/></svg></span>歯並びが悪い</div>
      <div><span class="ck"><svg width="16" height="16" viewBox="0 0 16 16"><path d="M3 8l3 3 7-7" stroke="#fff" stroke-width="2.4" fill="none"/></svg></span>インプラントが不安</div>
      <div><span class="ck"><svg width="16" height="16" viewBox="0 0 16 16"><path d="M3 8l3 3 7-7" stroke="#fff" stroke-width="2.4" fill="none"/></svg></span>口臭が気になる</div>
    </div>

    <h2 class="sec-head">診療項目</h2>
    <div class="menu-grid">
      <figure><div class="ph" role="img" aria-label="一般歯科の写真"></div>一般歯科</figure>
      <figure><div class="ph" role="img" aria-label="小児歯科の写真"></div>小児歯科</figure>
      <figure><div class="ph" role="img" aria-label="入れ歯の写真"></div>入れ歯（義歯）</figure>
      <figure><div class="ph" role="img" aria-label="口腔外科の写真"></div>口腔外科</figure>
      <figure><div class="ph" role="img" aria-label="インプラントの写真"></div>インプラント治療</figure>
      <figure><div class="ph" role="img" aria-label="審美歯科の写真"></div>審美歯科</figure>
      <figure><div class="ph" role="img" aria-label="矯正歯科の写真"></div>矯正歯科</figure>
      <figure><div class="ph" role="img" aria-label="ホワイトニングの写真"></div>ホワイトニング</figure>
      <figure><div class="ph" role="img" aria-label="歯周病治療の写真"></div>歯周病</figure>
      <figure><div class="ph" role="img" aria-label="予防歯科の写真"></div>予防歯科</figure>
    </div>
    <div class="recruit-banner"><span class="ph" role="img" aria-label="スタッフの写真"></span><div><b>私たちと一緒に働きませんか？</b><span>歯科医師・衛生士募集</span></div></div>

    <h2 class="sec-head">診療時間 / アクセス</h2>
    <div class="access">
      <div class="left">
        <table class="hours">
          <tr><th>診療時間</th><th>月</th><th>火</th><th>水</th><th>木</th><th>金</th><th>土</th><th>日</th></tr>
          <tr><td>9:00〜12:30</td><td class="o">●</td><td class="o">●</td><td class="o">●</td><td>／</td><td class="o">●</td><td class="o">●</td><td>／</td></tr>
          <tr><td>14:30〜18:30</td><td class="o">●</td><td class="o">●</td><td class="o">●</td><td>／</td><td class="o">●</td><td class="o">▲</td><td>／</td></tr>
        </table>
        <div class="tel"><svg width="26" height="26" viewBox="0 0 24 24"><path fill="#ef8a1c" d="M6.6 10.8a15 15 0 0 0 6.6 6.6l2.2-2.2c.3-.3.7-.4 1-.2 1.1.4 2.3.6 3.6.6.6 0 1 .4 1 1V20c0 .6-.4 1-1 1A17 17 0 0 1 3 4c0-.6.4-1 1-1h3.5c.6 0 1 .4 1 1 0 1.3.2 2.5.6 3.6.1.3 0 .7-.2 1z"/></svg>0595-00-1234</div>
        <p class="addr">〒000-0000 緑ヶ丘市さくら町1丁目2-3</p>
        <div class="card-note"><div class="hd">各種クレジット取扱い</div><div class="bd">取り扱いできるクレジットを表記</div></div>
      </div>
      <div class="map-box" role="img" aria-label="医院周辺の地図">
        <svg width="34" height="46" viewBox="0 0 24 32"><path fill="#ef8a1c" d="M12 0C5.4 0 0 5.2 0 11.7 0 20.4 12 32 12 32s12-11.6 12-20.3C24 5.2 18.6 0 12 0z"/><circle cx="12" cy="11.5" r="4.5" fill="#fff"/></svg>
      </div>
    </div>

    <div class="news-cols">
      <section>
        <h2 class="sec-head">新着情報</h2>
        <ul>
          <li><time>2016/10/01</time>タイトル/タイトル/タイトル</li>
          <li><time>2016/10/01</time>タイトル/タイトル/タイトル</li>
          <li><time>2016/10/01</time>タイトル/タイトル/タイトル</li>
          <li><time>2016/10/01</time>タイトル/タイトル/タイトル</li>
        </ul>
        <span class="all">› 新着情報一覧はこちら</span>
      </section>
      <section>
        <h2 class="sec-head">医院トピックス</h2>
        <ul>
          <li><time>2016/10/01</time>タイトル/タイトル/タイトル</li>
          <li><time>2016/10/01</time>タイトル/タイトル/タイトル</li>
          <li><time>2016/10/01</time>タイトル/タイトル/タイトル</li>
          <li><time>2016/10/01</time>タイトル/タイトル/タイトル</li>
        </ul>
        <span class="all">› 医院トピックス一覧はこちら</span>
      </section>
    </div>
  </main>
</div>

<div class="map-band" role="img" aria-label="医院周辺の広域地図">
  <svg width="44" height="58" viewBox="0 0 24 32"><path fill="#ef8a1c" d="M12 0C5.4 0 0 5.2 0 11.7 0 20.4 12 32 12 32s12-11.6 12-20.3C24 5.2 18.6 0 12 0z"/><circle cx="12" cy="11.5" r="4.5" fill="#fff"/></svg>
</div>

<footer class="site-footer">
  <div class="wrap">
    <div class="foot-row">
      <div>
        <div class="foot-brand"><span class="brand-mark"></span><span class="brand-name">みどり歯科クリニック</span></div>
        <div class="tel"><svg width="26" height="26" viewBox="0 0 24 24"><path fill="#ef8a1c" d="M6.6 10.8a15 15 0 0 0 6.6 6.6l2.2-2.2c.3-.3.7-.4 1-.2 1.1.4 2.3.6 3.6.6.6 0 1 .4 1 1V20c0 .6-.4 1-1 1A17 17 0 0 1 3 4c0-.6.4-1 1-1h3.5c.6 0 1 .4 1 1 0 1.3.2 2.5.6 3.6.1.3 0 .7-.2 1z"/></svg>0595-00-1234</div>
        <p class="addr">〒000-0000 緑ヶ丘市さくら町1丁目2-3</p>
      </div>
      <table class="hours">
        <tr><th>診療時間</th><th>月</th><th>火</th><th>水</th><th>木</th><th>金</th><th>土</th><th>日</th></tr>
        <tr><td>9:00〜12:30</td><td class="o">●</td><td class="o">●</td><td class="o">●</td><td>／</td><td class="o">●</td><td class="o">●</td><td>／</td></tr>
        <tr><td>14:30〜18:30</td><td class="o">●</td><td class="o">●</td><td class="o">●</td><td>／</td><td class="o">●</td><td class="o">▲</td><td>／</td></tr>
      </table>
    </div>
    <nav class="foot-links">
      <a href="#">トップ</a><a href="#">一般歯科</a><a href="#">審美歯科</a><a href="#">ホワイトニング</a><a href="#">設備紹介</a><a href="#">初めての方へ</a>
      <a href="#">院長紹介</a><a href="#">小児歯科</a><a href="#">インプラント治療</a><a href="#">歯周病</a><a href="#">アクセス</a><a href="#">求人情報</a>
      <a href="#">診療内容</a><a href="#">入れ歯（義歯）</a><a href="#">矯正歯科</a><a href="#">予防歯科</a><a href="#">費用について</a><a href="#">医院トピックス</a>
      <a href="#">新着情報</a><a href="#">口腔外科</a><a href="#">患者様の声</a>
    </nav>
  </div>
  <p class="copyright">© 2016 みどり歯科クリニック All Rights Reserved.</p>
</footer>
</body>
</html>
```